Simple Webpage for Company that offer IT Security Services

Company Type: Penetration Tests, IT Security Services, Security Audits
Company Name: VaultHaven
Navigation Style: similar to https://www.brivanta-example.com/en/ with Top Navigation (and submenu's)
Top Navigation Items: Services, About Us, Contact
Industry/Entity Type
It Company
Coding
Coded - Design and coding required

```html
<!DOCTYPE html>
<html lang="en">
<head>
<meta charset="utf-8">
<title>VaultHaven – IT Security Services</title>
<link href="https://fonts.googleapis.com/css2?family=Ubuntu:ital,wght@0,400;0,500;0,700;1,500;1,700&family=Open+Sans:ital,wght@0,400;0,600;0,700;1,400;1,600&display=swap" rel="stylesheet">
<style>
:root{
  --blue:#1e88c9;
  --blue-dark:#1565a8;
  --navy:#0f1c2b;
  --band:#2a6aa6;
  --ink:#2f2f2f;
  --text:#7a7a7a;
  --line:#e3e3e3;
  --footer:#f4f4f4;
  --white:#ffffff;
}
*{margin:0;padding:0;box-sizing:border-box}
html,body{width:1200px;height:3061px;overflow:hidden}
body{position:relative;background:var(--white);font-family:"Open Sans",Arial,sans-serif;color:var(--ink)}
.abs{position:absolute}
h1,h2,h3,h4{font-family:"Ubuntu",Arial,sans-serif}

/* header */
.site-header{position:absolute;left:0;top:0;width:1200px;height:96px;background:var(--white);z-index:5}
.brand{position:absolute;left:98px;top:26px;display:flex;align-items:center;gap:10px;font-family:"Ubuntu",sans-serif;font-weight:700;font-size:31px;color:var(--blue)}
.brand-dot{width:26px;height:26px;border-radius:50%;background:var(--blue)}
.main-nav{position:absolute;right:98px;top:0;height:96px;display:flex;align-items:center;gap:30px;font-family:"Ubuntu",sans-serif;font-weight:500;font-size:14px;color:#333}
.main-nav a{color:inherit;text-decoration:none;position:relative;padding:8px 0}
.main-nav a.active{color:var(--blue)}
.main-nav a.active::after{content:"";position:absolute;left:0;right:0;bottom:-8px;height:2px;background:var(--blue)}

/* hero */
.hero{left:0;top:96px;width:1200px;height:560px;background:linear-gradient(100deg,#3c3430 0%,#5a6470 35%,#1e3a66 55%,#4a4a3e 80%,#3b4230 100%);clip-path:polygon(0 0,100% 0,100% 486px,50% 556px,0 486px)}
.hero-title{left:98px;top:192px;font-size:45px;font-weight:700;color:var(--white);letter-spacing:1px}
.hero-text{left:98px;top:250px;width:300px;font-size:13.5px;font-weight:600;line-height:20px;color:var(--white)}
.btn-solid{display:inline-flex;align-items:center;gap:6px;background:var(--blue);color:var(--white);font-family:"Ubuntu",sans-serif;font-size:13px;padding:0 18px;height:34px;text-transform:uppercase}
.hero .btn-solid{position:absolute;left:98px;top:326px}
.slider-dots{left:570px;top:498px;display:flex;gap:4px}
.slider-dots span{width:12px;height:12px;border:2px solid #ddd;background:#777}
.slider-dots span.on{background:#fff}
.hero-edge{left:0;top:570px;width:1200px;height:90px}

/* section headings */
.section-title{width:1200px;left:0;text-align:center;font-size:36px;font-weight:700;color:#333;letter-spacing:.5px}
.section-sub{width:1200px;left:0;text-align:center;font-size:12px;color:#555}

/* services */
.service{width:300px;text-align:center}
.service svg{display:block;margin:0 auto}
.service h3{margin-top:26px;font-size:17px;font-weight:500;color:#333;text-transform:uppercase}
.service p{margin-top:12px;font-size:12.5px;line-height:21px;color:var(--text)}
.service .more{display:block;margin-top:14px;font-size:14px;color:#666}
.divider{width:1px;height:230px;background:var(--line)}

/* welcome */
.welcome{left:0;top:1148px;width:1200px;height:560px;background:linear-gradient(90deg,#0c1624 0%,#14273d 45%,#1a3150 70%,#0e1a2a 100%);clip-path:polygon(0 0,50% 70px,100% 0,100% 490px,50% 560px,0 490px)}
.welcome-photo{left:560px;top:0;width:640px;height:560px;background:radial-gradient(ellipse at 60% 55%,#2a4a72 0%,#1a2f4c 45%,rgba(14,26,42,0) 80%)}
.welcome h2{position:absolute;left:98px;top:176px;font-size:34px;font-weight:500;color:var(--white)}
.welcome p{position:absolute;left:98px;width:520px;font-size:12px;font-weight:600;line-height:19px;color:var(--white)}
.btn-outline{display:inline-flex;align-items:center;justify-content:center;gap:5px;border:1px solid #bbb;font-family:"Ubuntu",sans-serif;font-size:12px;text-transform:uppercase;height:30px;padding:0 16px}
.welcome .btn-outline{position:absolute;left:98px;top:380px;color:var(--white);border-color:#ddd}

/* it services cards */
.title-rule{left:576px;top:1858px;width:48px;height:3px;background:var(--blue)}
.card{width:312px}
.card-img{height:178px;border:4px solid #e8e8e8;box-shadow:0 0 0 1px #d6d6d6}
.card h4{margin-top:30px;font-size:14px;font-weight:700;color:#333;text-transform:uppercase}
.card p{margin-top:12px;font-size:12px;line-height:18px;color:var(--text)}
.card .btn-outline{margin-top:20px;color:#444;height:30px;padding:0 12px;font-size:11px;border-color:#999}

/* testimonial */
.testimonial{left:0;top:2268px;width:1200px;height:456px;background:linear-gradient(180deg,#2c6ca8 0%,#2a67a2 50%,#1f5a95 100%);clip-path:polygon(0 0,50% 72px,100% 0,100% 374px,50% 456px,0 374px)}
.quote-mark{left:0;width:1200px;top:150px;text-align:center;font-family:Georgia,serif;font-size:54px;font-weight:700;color:var(--white);line-height:40px}
.quote{left:220px;width:760px;top:196px;text-align:center;font-size:13.5px;font-style:italic;line-height:24px;color:var(--white)}
.author{left:512px;top:274px;display:flex;align-items:center;gap:16px}
.author-photo{width:50px;height:56px;background:linear-gradient(#d9c4ae,#9b8470);clip-path:polygon(50% 0,100% 25%,100% 75%,50% 100%,0 75%,0 25%)}
.author-name{font-family:"Open Sans",sans-serif;font-style:italic;font-weight:700;font-size:14px;line-height:20px;color:var(--white)}

/* footer */
.footer{left:0;top:2640px;width:1200px;height:380px;background:var(--footer);z-index:-1}
.foot-brand{left:98px;top:2752px;font-size:28px}
.foot-about{left:98px;top:2818px;width:230px;font-size:12px;line-height:19px;color:#555}
.socials{left:98px;top:2892px;display:flex;gap:7px}
.socials span{width:24px;height:24px;border:1px solid #888;border-radius:50%}
.foot-col h4{font-size:16px;font-weight:500;color:#333;text-transform:uppercase;letter-spacing:.3px}
.foot-col p{font-size:12px;line-height:19px;color:#555}
.news-input{width:246px;height:40px;margin-top:18px;border:1px solid #ddd;background:#fff;font-size:12px;color:#555;padding:0 14px;display:flex;align-items:center}
.news-btn{margin-top:14px;display:inline-flex;align-items:center;height:32px;padding:0 16px;background:var(--blue-dark);color:#fff;font-family:"Ubuntu",sans-serif;font-size:13px;text-transform:uppercase}
.contact-list{list-style:none;margin-top:16px}
.contact-list li{display:flex;gap:12px;font-size:12.5px;line-height:20px;color:#555;margin-bottom:12px}
.contact-list svg{flex:none;margin-top:3px}
.links{list-style:none;margin-top:14px}
.links li{font-size:11.5px;line-height:21px;color:#555}
.copyright{left:0;top:3000px;width:1200px;border-top:1px solid #ddd;padding-top:14px;text-align:center;font-size:11.5px;color:#555}
</style>
</head>
<body>

<header class="site-header">
  <div class="brand"><span class="brand-dot"></span>VaultHaven</div>
  <nav class="main-nav">
    <a class="active">HOME</a>
    <a>ABOUT US</a>
    <a>OUR SERVICES</a>
    <a>NEWS &amp; MEDIA</a>
    <a>CONTACT US</a>
    <svg width="14" height="14" viewBox="0 0 14 14"><circle cx="6" cy="6" r="4.3" fill="none" stroke="#333" stroke-width="1.8"/><line x1="9.2" y1="9.2" x2="13" y2="13" stroke="#333" stroke-width="2"/></svg>
  </nav>
</header>

<section class="hero abs" role="img" aria-label="Office scene with people working at a computer showing a padlock on a circuit screen">
  <h1 class="hero-title abs">VAULTHAVEN</h1>
  <p class="hero-text abs">Sed ut perspiciatis unde omnis iste natus error sit voluptatem accusantium dolorem-que laudantium, totam</p>
  <span class="btn-solid">Read more
    <svg width="11" height="11" viewBox="0 0 11 11"><circle cx="5.5" cy="5.5" r="5" fill="#fff"/><path d="M4.5 3l2.5 2.5L4.5 8" fill="none" stroke="#1e88c9" stroke-width="1.5"/></svg></span>
  <div class="slider-dots abs"><span class="on"></span><span></span><span></span><span></span></div>
</section>
<svg class="hero-edge abs" viewBox="0 0 1200 90" width="1200" height="90">
  <polyline points="0,12 600,82 1200,12" fill="none" stroke="#1e88c9" stroke-width="3"/>
</svg>

<h2 class="section-title abs" style="top:718px">OUR SERVICES</h2>
<p class="section-sub abs" style="top:766px">We provide IT security services</p>

<div class="divider abs" style="left:415px;top:900px"></div>
<div class="divider abs" style="left:785px;top:900px"></div>

<div class="service abs" style="left:80px;top:830px">
  <svg width="124" height="130" viewBox="0 0 124 130"><polygon points="62,2 120,34 120,96 62,128 4,96 4,34" fill="#1e88c9" stroke="#5fb3e4" stroke-width="3"/>
    <rect x="40" y="46" width="44" height="30" rx="2" fill="none" stroke="#fff" stroke-width="3"/><line x1="52" y1="86" x2="72" y2="86" stroke="#fff" stroke-width="3"/><line x1="62" y1="76" x2="62" y2="86" stroke="#fff" stroke-width="3"/>
    <path d="M55 56l-5 5 5 5M69 56l5 5-5 5M64 54l-4 14" fill="none" stroke="#fff" stroke-width="2"/></svg>
  <h3>Penetration Tests</h3>
  <p>Sed ut perspiciatis unde omnis iste natus error sit voluptatem accusantium doloremque laudantium, totam rem aperiam, eaque ipsa quae</p>
  <span class="more">Read More ↘</span>
</div>

<div class="service abs" style="left:450px;top:830px">
  <svg width="124" height="130" viewBox="0 0 124 130"><polygon points="62,2 120,34 120,96 62,128 4,96 4,34" fill="#1e88c9" stroke="#5fb3e4" stroke-width="3"/>
    <rect x="48" y="60" width="28" height="22" rx="2" fill="none" stroke="#fff" stroke-width="3"/><path d="M54 60v-6a8 8 0 0 1 16 0v6" fill="none" stroke="#fff" stroke-width="3"/>
    <path d="M40 56h-8M40 70h-8M40 84h-8M84 56h8M84 70h8M84 84h8" stroke="#fff" stroke-width="2"/><circle cx="62" cy="71" r="2.5" fill="#fff"/></svg>
  <h3>IT Security Services</h3>
  <p>Sed ut perspiciatis unde omnis iste natus error sit voluptatem accusantium doloremque laudantium, totam rem aperiam, eaque ipsa quae</p>
  <span class="more">Read More ↘</span>
</div>

<div class="service abs" style="left:820px;top:830px">
  <svg width="124" height="130" viewBox="0 0 124 130"><polygon points="62,2 120,34 120,96 62,128 4,96 4,34" fill="#1e88c9" stroke="#5fb3e4" stroke-width="3"/>
    <path d="M62 40l22 8v16c0 14-10 22-22 27-12-5-22-13-22-27V48z" fill="none" stroke="#fff" stroke-width="3"/><path d="M52 65l7 7 13-14" fill="none" stroke="#fff" stroke-width="3"/></svg>
  <h3>Security Audits</h3>
  <p>Sed ut perspiciatis unde omnis iste natus error sit voluptatem accusantium doloremque laudantium, totam rem aperiam, eaque ipsa quae</p>
  <span class="more">Read More ↘</span>
</div>

<section class="welcome abs">
  <div class="welcome-photo abs" role="img" aria-label="Businessman in a suit holding a glowing security shield between his hands"></div>
  <h2>WELCOME TO VAULTHAVEN</h2>
  <p style="top:232px">Sed ut perspiciatis unde omnis iste natus error sit voluptatem accusantium doloremque laudantium, totam rem aperiam, eaque ipsa quae ab illo inventore veritatis et quasi architecto beatae vitae dicta sunt explicabo. Nemo enim ipsam</p>
  <p style="top:304px">Voluptas sit aspernatur aut odit aut fugit, sed quia consequuntur magni dolores eos qui ratione voluptatem sequi nesciunt. Neque porro quisquam est, qui dolorem ipsum quia dolor sit amet, consectetur, adipisci velit,</p>
  <span class="btn-outline">Read more</span>
</section>

<h2 class="section-title abs" style="top:1800px">IT SECURITY SERVICES</h2>
<div class="title-rule abs"></div>

<div class="card abs" style="left:98px;top:1902px">
  <div class="card-img" role="img" aria-label="Security analyst working at a computer with code on screen" style="background:linear-gradient(135deg,#1d3f5e,#3a6f8f 55%,#17324a)"></div>
  <h4>Sed ut perspiciatis unde omnis</h4>
  <p>Sed ut perspiciatis unde omnis iste natus error sit voluptatem accusantium doloremque laudantium, totam</p>
  <span class="btn-outline">Read more ⊕</span>
</div>

<div class="card abs" style="left:444px;top:1902px">
  <div class="card-img" role="img" aria-label="Team of colleagues discussing work around a laptop" style="background:linear-gradient(135deg,#9ec3d8,#e2e6e4 50%,#6f9fbc)"></div>
  <h4>Sed ut perspiciatis unde omnis</h4>
  <p>Sed ut perspiciatis unde omnis iste natus error sit voluptatem accusantium doloremque laudantium, totam</p>
  <span class="btn-outline">Read more ⊕</span>
</div>

<div class="card abs" style="left:790px;top:1902px">
  <div class="card-img" role="img" aria-label="Technician working in a server room with network racks" style="background:linear-gradient(135deg,#4a4e55,#9aa0a6 50%,#3c4048)"></div>
  <h4>Sed ut perspiciatis unde omnis</h4>
  <p>Sed ut perspiciatis unde omnis iste natus error sit voluptatem accusantium doloremque laudantium, totam</p>
  <span class="btn-outline">Read more ⊕</span>
</div>

<div class="footer abs"></div>

<section class="testimonial abs" role="img" aria-label="Blurred office background in blue tones">
  <div class="quote-mark abs">“</div>
  <p class="quote abs">“ Sed ut perspiciatis unde omnis iste natus error sit voluptatem accusantium doloremque laudantium, totam rem aperiam, eaque ipsa quae ab illo inventore veritatis et quasi architecto beatae vitae dicta sunt explicabo. Nemo enim ipsam voluptatem quia voluptas sit aspernatur aut odit aut fugit, sed quia consequuntur .</p>
  <div class="author abs">
    <div class="author-photo" role="img" aria-label="Portrait of the client"></div>
    <div class="author-name">- Rafael Ortiz<br>VaultHaven</div>
  </div>
</section>

<div class="brand abs foot-brand"><span class="brand-dot" style="width:22px;height:22px"></span>VaultHaven</div>
<p class="foot-about abs">Nemo enim ipsam voluptatem quia voluptas sit aspernatur aut odit aut fugit, sed quia consequuntur magni dolores</p>
<div class="socials abs"><span></span><span></span><span></span><span></span></div>

<div class="foot-col abs" style="left:400px;top:2768px;width:250px">
  <h4>Sign up for newsletter</h4>
  <p style="margin-top:12px">Excepteur sint occaecat cupidatat non proident, sunt in culpa qui officia deserunt</p>
  <div class="news-input">Enter email</div>
  <span class="news-btn">Subscription</span>
</div>

<div class="foot-col abs" style="left:722px;top:2768px;width:220px">
  <h4>Contact us</h4>
  <ul class="contact-list">
    <li><svg width="12" height="15" viewBox="0 0 12 15"><path d="M6 1a5 5 0 0 1 5 5c0 4-5 8-5 8S1 10 1 6a5 5 0 0 1 5-5z" fill="none" stroke="#666" stroke-width="1.6"/><circle cx="6" cy="6" r="1.8" fill="#666"/></svg><span>VaultHaven 12, Suite<br>300, Fairview, GA 30999</span></li>
    <li><svg width="12" height="13" viewBox="0 0 12 13"><path d="M2 1l3 0 1 3-2 1.5c1 2 2 3 3.5 3.5L9 7l3 1v3c-6 0-10-4-10-10z" fill="#666"/></svg><span>Phone: &nbsp;(555) 010-4827</span></li>
    <li><svg width="12" height="10" viewBox="0 0 12 10"><rect x="0" y="1" width="12" height="8" fill="#666"/><path d="M0 1l6 4 6-4" fill="none" stroke="#f4f4f4" stroke-width="1.2"/></svg><span>info@vaulthaven-example.com</span></li>
  </ul>
</div>

<div class="foot-col abs" style="left:995px;top:2768px;width:120px">
  <h4>Quick links</h4>
  <ul class="links">
    <li>Home</li><li>Our Services</li><li>About Us</li><li>Careers</li><li>VaultHaven</li><li>Contact Us</li>
  </ul>
</div>

<p class="copyright abs">©2017 VaultHaven.. All Rights Reserved.</p>

</body>
</html>
```